'Tarvel' a financial/crypto-currency exchange in the middle east

On the card we need 1) Name 2) title 3) email address 4) phone number using the same colors and theme as the logo. On one side we just want the logo and we want the whole card to be in blue (same blue as logo) with the logo in the back being white.
Industry/Entity Type
Financial

```html
<!DOCTYPE html>
<html lang="en">
<head>
<meta charset="utf-8">
<title>Tarvel Business Card</title>
<link href="https://fonts.googleapis.com/css2?family=Montserrat:wght@600;700&family=Open+Sans:wght@400;600&display=swap" rel="stylesheet">
<style>
  :root {
    --brand-blue: #1a8fd3;
    --brand-blue-soft: #3aa0dc;
    --brand-blue-ring: #5fb4e4;
    --paper: #f5f6f7;
    --pale-blue: #cfe4f1;
    --ink: #4a4f55;
    --silver: #e4e6e8;
    --stage: #2b2d30;
  }
  * { margin: 0; padding: 0; box-sizing: border-box; }
  html, body { width: 1200px; height: 896px; overflow: hidden; }
  body { background: var(--stage); position: relative; font-family: "Open Sans", sans-serif; }

  .card {
    position: absolute;
    left: 352px;
    width: 486px;
    height: 277px;
    border-radius: 16px;
    overflow: hidden;
  }
  .card--front { top: 162px; background: var(--brand-blue); }
  .card--back { top: 469px; background: var(--paper); }

  .card__decor { position: absolute; inset: 0; }

  .brand {
    position: absolute;
    display: flex;
    align-items: center;
    gap: 12px;
    font-family: "Montserrat", sans-serif;
    font-weight: 700;
    font-size: 37px;
    letter-spacing: 0.2px;
  }
  .brand__dot { border-radius: 50%; flex: none; }
  .card--front .brand { left: 128px; top: 104px; color: var(--silver); }
  .card--front .brand__dot { width: 66px; height: 66px; background: var(--silver); }
  .card--back .brand { left: 32px; top: 30px; color: var(--brand-blue); }
  .card--back .brand__dot { width: 66px; height: 66px; border: 3px solid var(--brand-blue); }

  .front__web {
    position: absolute;
    left: 180px;
    top: 240px;
    font-size: 11.5px;
    font-weight: 600;
    letter-spacing: 0.8px;
    color: #e6f2fa;
  }

  .accent-bar {
    position: absolute;
    left: 0;
    top: 118px;
    width: 6px;
    height: 34px;
    background: var(--brand-blue);
  }
  .contact { position: absolute; left: 32px; top: 116px; color: var(--ink); }
  .contact__name {
    font-family: "Montserrat", sans-serif;
    font-weight: 700;
    font-size: 18px;
    color: var(--brand-blue);
    letter-spacing: 0.4px;
    line-height: 22px;
  }
  .contact__title { font-size: 11px; line-height: 16px; margin-bottom: 10px; }
  .contact__address { font-size: 11px; line-height: 18px; margin-bottom: 6px; }
  .contact__list { list-style: none; font-size: 11px; line-height: 18px; }
  .contact__list li { display: flex; align-items: center; gap: 8px; }
  .contact__icon { width: 10px; height: 10px; flex: none; }
</style>
</head>
<body>

<section class="card card--front" aria-label="Card front">
  <svg class="card__decor" width="486" height="277" viewBox="0 0 486 277" aria-hidden="true">
    <circle cx="-8" cy="138" r="146" fill="var(--brand-blue-soft)"/>
    <circle cx="-8" cy="138" r="134" fill="none" stroke="var(--brand-blue-ring)" stroke-width="5"/>
  </svg>
  <div class="brand"><span class="brand__dot"></span>Tarvel</div>
  <p class="front__web">www.tarvel.example</p>
</section>

<section class="card card--back" aria-label="Card back">
  <svg class="card__decor" width="486" height="277" viewBox="0 0 486 277" aria-hidden="true">
    <circle cx="492" cy="137" r="152" fill="var(--pale-blue)"/>
    <circle cx="492" cy="137" r="136" fill="none" stroke="#ffffff" stroke-width="5"/>
  </svg>
  <div class="brand"><span class="brand__dot"></span>Tarvel</div>
  <span class="accent-bar"></span>
  <div class="contact">
    <h1 class="contact__name">DANA KOREL</h1>
    <p class="contact__title">President</p>
    <p class="contact__address">14 Harbor Gate Road,<br>Suite 210&nbsp; - &nbsp;Dubai, UAE 00000</p>
    <ul class="contact__list">
      <li>
        <svg class="contact__icon" viewBox="0 0 10 10" aria-hidden="true"><path d="M2 0.5 L3.6 2.6 L2.7 3.6 C3.3 5 4.6 6.4 6.2 7.2 L7.2 6.3 L9.5 7.8 L8.4 9.5 C4.5 9.2 0.8 5.4 0.5 1.6 Z" fill="var(--brand-blue)"/></svg>
        (971) 555-0142
      </li>
      <li>
        <svg class="contact__icon" viewBox="0 0 10 10" aria-hidden="true"><rect x="0.5" y="2" width="9" height="6.5" fill="var(--brand-blue)"/><path d="M0.8 2.3 L5 5.6 L9.2 2.3" fill="none" stroke="#fff" stroke-width="0.9"/></svg>
        dana@tarvel.example
      </li>
      <li>
        <svg class="contact__icon" viewBox="0 0 10 10" aria-hidden="true"><circle cx="5" cy="5" r="4.3" fill="none" stroke="var(--brand-blue)" stroke-width="1.1"/><ellipse cx="5" cy="5" rx="1.8" ry="4.3" fill="none" stroke="var(--brand-blue)" stroke-width="0.9"/><path d="M0.8 5 H9.2" stroke="var(--brand-blue)" stroke-width="0.9"/></svg>
        www.tarvel.example
      </li>
    </ul>
  </div>
</section>

</body>
</html>
```